Corporate Letterhead

Looking for a new corporate letterhead design. Our colors are orange and gray.

We'd like it if the below could be included somehow in the letterhead.                                       

Partnerships | Results | Quality

• Logo, Company Name, Address, Phone #, Fax #, Web address, Email address (optional), the phrase "A Service Disable Veteran Owned Small Business".

```html
<!DOCTYPE html>
<html lang="en">
<head>
<meta charset="utf-8">
<title>Vantora Systems, Inc. — Letterhead</title>
<link rel="stylesheet" href="https://fonts.googleapis.com/css2?family=Arimo:wght@400;700&family=Caveat:wght@500&display=swap">
<style>
  :root {
    --orange: #f7941d;
    --rule-gray: #8c8c8c;
    --text-gray: #7a7a7a;
    --paper: #fefefe;
  }
  html, body {
    margin: 0;
    padding: 0;
    overflow: hidden;
    background: var(--paper);
  }
  .letterhead {
    position: relative;
    width: 848px;
    height: 1200px;
    background: var(--paper);
    overflow: hidden;
    font-family: "Arimo", Arial, sans-serif;
  }
  .brand {
    position: absolute;
    left: 28px;
    top: 18px;
    width: 330px;
    display: flex;
    align-items: center;
    gap: 12px;
  }
  .brand-dot {
    flex: none;
    width: 50px;
    height: 50px;
    border-radius: 50%;
    background: var(--orange);
  }
  .brand-name {
    font-family: "Arimo", Arial, sans-serif;
    font-weight: 700;
    font-size: 24px;
    line-height: 1;
    color: var(--orange);
    letter-spacing: 0.3px;
    text-transform: uppercase;
    white-space: nowrap;
  }
  .tagline {
    position: absolute;
    left: 36px;
    top: 85px;
    width: 330px;
    font-family: "Caveat", cursive;
    font-weight: 500;
    font-size: 19px;
    color: var(--orange);
    line-height: 1;
    white-space: nowrap;
  }
  .header-pattern {
    position: absolute;
    left: 362px;
    top: 5px;
    width: 480px;
    height: 68px;
    background: linear-gradient(90deg, rgba(247,148,29,0) 0%, rgba(247,148,29,0.45) 30%, var(--orange) 55%, var(--orange) 100%);
  }
  .contact {
    position: absolute;
    top: 75px;
    margin: 0;
    font-size: 11.5px;
    line-height: 14px;
    color: var(--orange);
  }
  .contact-lines { left: 386px; }
  .contact-address { right: 7px; text-align: right; font-style: normal; }
  .header-rule {
    position: absolute;
    left: 0;
    top: 119px;
    width: 848px;
    height: 4px;
    background: var(--rule-gray);
  }
  .footer {
    position: absolute;
    left: 0;
    right: 0;
    bottom: 22px;
    text-align: center;
    font-size: 11px;
    line-height: 14px;
    color: var(--text-gray);
    letter-spacing: 0.5px;
  }
  .footer .values { color: var(--orange); font-weight: 700; }
</style>
</head>
<body>
  <div class="letterhead">
    <div class="brand">
      <span class="brand-dot"></span>
      <span class="brand-name">Vantora Systems, Inc</span>
    </div>
    <div class="tagline">A Service Disable Veteran Owned Small Business</div>

    <div class="header-pattern" role="img" aria-label="Decorative grid of orange squares fading in from the left with soft gray swoosh lines"></div>

    <p class="contact contact-lines">
      Telephone: (443) 555 0142<br>
      FAX: (410) 555-0187<br>
      E-mail: info@vantorasys.com
    </p>
    <address class="contact contact-address">
      Vantora Systems, Inc.<br>
      1420 Commerce Drive,<br>
      Suite 210, Linthicum, MD 21090
    </address>

    <div class="header-rule"></div>

    <p class="footer"><span class="values">Partnerships | Results | Quality</span> &nbsp;·&nbsp; www.vantorasys.com</p>
  </div>
</body>
</html>
```